Business Card Design Project

I require a business card for a new coaching business based in Melbourne with global clients. Both companies and individuals will retain our coaching services.

Target Market(s)

Both small business and large corporate in western speaking countries. Individuals requiring support and direction on issues such as fears, phobias, career, relationships, confidence, self esteem etc.

Industry/Entity Type

Business

Font styles to use
Sans Serif

Colors

Designer to choose colors to be used in the design.

Requirements
Must have
• White background to enhance the colours in the logo. Logo on the left.
Should not have
• The black and white version of the logo. Keep the colours.

```html
<!DOCTYPE html>
<html lang="en">
<head>
<meta charset="utf-8">
<title>Bright Shift Coaching – Business Card</title>
<link rel="stylesheet" href="https://fonts.googleapis.com/css2?family=Mulish:wght@300;400;700;800&display=swap">
<style>
  :root {
    --backdrop: #ebeced;
    --card: #ffffff;
    --ink: #2b2b2b;
    --ink-soft: #444444;
    --brand-grey: #6d6e71;
    --pink: #e5176b;
    --orange: #f0841e;
    --green: #8dc034;
    --blue: #0a7cc1;
  }
  * { box-sizing: border-box; margin: 0; padding: 0; }
  html, body {
    width: 1035px; height: 1200px; overflow: hidden;
    background: var(--backdrop);
    font-family: "Mulish", sans-serif;
  }
  .canvas { position: relative; width: 1035px; height: 1200px; }
  .card {
    position: absolute; width: 792px; height: 469px;
    background: var(--card); overflow: hidden;
    box-shadow: 0 8px 10px rgba(0,0,0,0.22);
  }
  .card--front { left: 115px; top: 88px; }
  .card--back  { left: 118px; top: 623px; }

  .colour-band {
    position: absolute; left: 0; bottom: 0; width: 100%; height: 70px;
    background: linear-gradient(180deg, var(--pink) 0%, var(--orange) 35%, var(--green) 65%, var(--blue) 100%);
    opacity: 0.9;
  }

  .brand { position: absolute; left: 190px; top: 82px; display: flex; align-items: center; gap: 28px; }
  .brand__dot { width: 120px; height: 120px; border-radius: 50%; background: var(--pink); }
  .brand__name {
    font-weight: 700; font-size: 39px; line-height: 1.02; color: var(--brand-grey);
    text-transform: uppercase; letter-spacing: -0.5px;
  }

  .person { position: absolute; right: 370px; top: 284px; text-align: right; }
  .person__name { font-weight: 800; font-size: 22px; color: var(--ink); }
  .person__role { font-weight: 300; font-size: 19px; color: var(--ink-soft); margin-top: 4px; }

  .divider { position: absolute; left: 434px; top: 264px; width: 3px; height: 103px; background: var(--blue); }

  .contact { position: absolute; left: 450px; top: 266px; list-style: none; }
  .contact__item {
    display: flex; align-items: center; height: 38px;
    font-size: 19px; font-weight: 300; color: var(--ink-soft);
  }
  .contact__icon { width: 34px; display: flex; justify-content: center; }
  .contact__icon svg { width: 20px; height: 20px; fill: none; stroke: var(--blue); stroke-width: 2; }

  .motto { position: absolute; left: 0; width: 100%; text-align: center; font-weight: 800; font-size: 27px; }
  .motto--pink { top: 160px; color: var(--pink); }
  .motto--blue { top: 236px; color: var(--blue); }
</style>
</head>
<body>
<main class="canvas">

  <section class="card card--front">
    <div class="brand">
      <span class="brand__dot"></span>
      <div class="brand__name">Bright Shift<br>Coaching</div>
    </div>

    <div class="person">
      <p class="person__name">Maren Holloway-Reid</p>
      <p class="person__role">Performance Consultant and Coach</p>
    </div>

    <span class="divider"></span>

    <ul class="contact">
      <li class="contact__item">
        <span class="contact__icon"><svg viewBox="0 0 24 24"><path d="M6 3l3 1 1 4-2 2c1 3 3 5 6 6l2-2 4 1 1 3-2 3C10 21 3 14 3 5z"/></svg></span>
        <span class="contact__text">+61 (0) 400 583 912</span>
      </li>
      <li class="contact__item">
        <span class="contact__icon"><svg viewBox="0 0 24 24"><rect x="3" y="6" width="18" height="12"/><path d="M3 6l9 7 9-7"/></svg></span>
        <span class="contact__text">maren.hr@brightshift.example</span>
      </li>
      <li class="contact__item">
        <span class="contact__icon"></span>
        <span class="contact__text">ABN58310946271</span>
      </li>
    </ul>

    <div class="colour-band" role="img" aria-label="Decorative multicolour wave band in pink, orange, green and blue"></div>
  </section>

  <section class="card card--back">
    <p class="motto motto--pink">The mind is more powerful than the body.</p>
    <p class="motto motto--blue">Give yourself permission to shine.</p>

    <div class="colour-band" role="img" aria-label="Decorative multicolour wave band in pink, orange, green and blue"></div>
  </section>

</main>
</body>
</html>
```